Simple but elegant business card/logo design for exclusive beauty business

We need a logo designed for a new elegant and exclusive beauty business called "R". The logo itself should be a stylistic and custom design for the letter "R". We would like the business card to have the logo as the centrepiece on a clean background. Gold Logo on black background or silver on white background.

The business card details should be displayed centre of the card. Details are as follows:

Tamsin Earle
Facebook: /shinesoftlyr
Instagram: /shinesoftlyr

The words "Shine Softly" should also appear somewhere on the card.

Industry/Entity Type

Business

Logo Text

G

Requirements
Must have
• Design must be simple, clean and elegant
Should not have
• The design should not be cluttered

```html
<!DOCTYPE html>
<html lang="en">
<head>
<meta charset="utf-8">
<title>Shine Softly – Business Card</title>
<link rel="stylesheet" href="https://fonts.googleapis.com/css2?family=Questrial&display=swap">
<style>
  :root {
    --canvas: #ffffff;
    --ink: #222220;
    --gold: #e2c53f;
    --gold-deep: #dba92a;
    --gold-edge: #e0bd3a;
    --gold-light: #ede560;
    --white: #ffffff;
  }
  * { margin: 0; padding: 0; box-sizing: border-box; }
  html, body {
    width: 1200px; height: 1200px; overflow: hidden;
    background: var(--canvas);
    font-family: "Questrial", "Century Gothic", sans-serif;
  }
  .card {
    position: absolute;
    left: 181px;
    width: 840px;
    height: 480px;
    overflow: hidden;
    box-shadow: 22px 26px 40px rgba(0,0,0,0.35);
  }
  .card--front { top: 78px; background: var(--ink); }
  .card--back {
    top: 615px;
    background: linear-gradient(90deg, var(--gold-edge) 0%, var(--gold-light) 38%, var(--gold-light) 55%, var(--gold-deep) 100%);
  }

  /* Front */
  .brand-mark {
    position: absolute;
    left: 334px; top: 100px;
    width: 172px; height: 172px;
    border-radius: 50%;
    border: 10px solid var(--gold);
  }
  .brand-name--front {
    position: absolute;
    left: 0; right: 0; top: 328px;
    text-align: center;
    color: var(--gold);
    font-size: 60px;
    letter-spacing: 10px;
    line-height: 1;
    white-space: nowrap;
  }

  /* Back */
  .side-band {
    position: absolute; left: 0; top: 0;
    width: 105px; height: 100%;
    background: var(--ink);
  }
  .detail {
    position: absolute;
    left: 105px;
    width: 406px; height: 56px;
    background: var(--ink);
    border-radius: 0 28px 28px 0;
    color: var(--white);
    display: flex; align-items: center;
    white-space: nowrap;
  }
  .detail--name { top: 114px; padding-left: 30px; font-size: 30px; letter-spacing: 4px; }
  .detail--handle-first { top: 213px; }
  .detail--handle-second { top: 311px; }
  .detail__icon {
    position: absolute; left: 30px; top: 10px;
    width: 37px; height: 37px;
    border-radius: 5px;
    background: var(--white);
  }
  .detail__handle {
    position: absolute; left: 97px;
    font-size: 24px; letter-spacing: 4px;
  }
  .brand-mark--small {
    position: absolute;
    left: 628px; top: 224px;
    width: 82px; height: 82px;
    border-radius: 50%;
    border: 7px solid var(--ink);
  }
  .brand-name--back {
    position: absolute;
    left: 569px; width: 200px; top: 342px;
    text-align: center;
    color: var(--ink);
    font-size: 22px;
    letter-spacing: 4px;
    line-height: 1;
    white-space: nowrap;
  }
</style>
</head>
<body>
  <section class="card card--front" aria-label="Card front">
    <div class="brand-mark" aria-hidden="true"></div>
    <p class="brand-name brand-name--front">Shine Softly</p>
  </section>

  <section class="card card--back" aria-label="Card back">
    <div class="side-band"></div>
    <p class="detail detail--name">Tamsin Earle</p>
    <p class="detail detail--handle-first"><span class="detail__icon" aria-hidden="true"></span><span class="detail__handle">/shinesoftlyr</span></p>
    <p class="detail detail--handle-second"><span class="detail__icon" aria-hidden="true"></span><span class="detail__handle">/shinesoftlyr</span></p>
    <div class="brand-mark--small" aria-hidden="true"></div>
    <p class="brand-name brand-name--back">Shine Softly</p>
  </section>
</body>
</html>
```